DOG DAYCARE BILLBOARD

Design a bold exciting billboard that can be read easily from a distance! Our goal is brand awareness and showcasing the services we offer (Boarding, Grooming, Daycare, and Training.
we would like to see examples with the phrase "your best friend's best day". Our name Bright Meadow Canine Activity Center (or just Bright Meadow might work better and could be bigger) and the services we provide.
(there are two examples of what we like included in the pictures)
you can find more information o our website at pawplayhub@mailnest.example.

```html
<!DOCTYPE html>
<html lang="en">
<head>
<meta charset="utf-8">
<title>Bright Meadow Billboard</title>
<link rel="stylesheet" href="https://fonts.googleapis.com/css2?family=Jost:wght@400;500;700;800&family=Michroma&display=swap">
<style>
  :root {
    --olive: #c2b530;
    --white: #ffffff;
    --ink: #161616;
    --dog-warm: #b0733a;
    --dog-light: #e6e2dc;
  }
  * { box-sizing: border-box; margin: 0; padding: 0; }
  html, body { width: 1200px; height: 1200px; overflow: hidden; background: var(--white); }
  body { position: relative; font-family: "Jost", Arial, sans-serif; }

  .billboard {
    position: absolute; left: 40px; top: 344px;
    width: 1120px; height: 512px;
    background: var(--white);
    border: 1px solid #444;
    overflow: hidden;
  }
  .band-top {
    position: absolute; left: 0; top: 0; width: 100%; height: 125px;
    background: var(--olive);
  }
  .band-bottom {
    position: absolute; left: 0; bottom: 0; width: 100%; height: 147px;
    background: var(--olive);
  }
  .brand-title {
    position: absolute; left: 170px; top: 14px;
    font-family: "Michroma", "Jost", sans-serif;
    font-size: 56px; letter-spacing: 1px;
    color: var(--white);
    transform: skewX(-14deg);
    white-space: nowrap;
    line-height: 1;
  }
  .tagline {
    position: absolute; left: 174px; top: 80px;
    font-weight: 700; font-size: 25px; color: var(--white);
    white-space: nowrap;
  }
  .headline {
    position: absolute; left: 48px; top: 146px;
    font-weight: 800; font-size: 46px; color: var(--ink);
    white-space: nowrap; letter-spacing: 0.5px;
  }
  .services {
    position: absolute; left: 450px; top: 205px;
    list-style: none;
  }
  .services li {
    position: relative; padding-left: 38px;
    font-weight: 800; font-size: 31px; line-height: 37px;
    color: var(--ink); white-space: nowrap;
  }
  .services li::before {
    content: ""; position: absolute; left: 0; top: 8px;
    width: 22px; height: 22px; border-radius: 50%;
    background: var(--olive);
  }
  .photo-left {
    position: absolute; left: 36px; top: 222px;
    width: 375px; height: 143px;
    border-radius: 120px 120px 0 0;
    background: linear-gradient(180deg, #8a5326 0%, var(--dog-warm) 55%, #d29a5e 100%);
  }
  .photo-right {
    position: absolute; left: 798px; top: 68px;
    width: 302px; height: 311px;
    border-radius: 100px 100px 24px 24px;
    background: linear-gradient(180deg, #f1efec 0%, var(--dog-light) 60%, #cfcac3 100%);
  }
  .brand-mark {
    position: absolute; left: 48px; top: 412px;
    display: flex; align-items: center; gap: 10px;
    font-weight: 700; font-size: 20px; color: var(--ink);
    white-space: nowrap;
  }
  .brand-mark .dot {
    width: 18px; height: 18px; border-radius: 50%; background: var(--ink);
  }
  .contact {
    position: absolute; left: 294px; top: 377px;
    color: var(--white); white-space: nowrap;
  }
  .contact .call { font-size: 34px; font-weight: 400; line-height: 48px; }
  .contact .call strong { font-size: 46px; font-weight: 700; }
  .contact .line { font-size: 24px; font-weight: 400; line-height: 31px; }
  .contact .line strong { font-weight: 700; }
  .address {
    position: absolute; left: 852px; top: 384px;
    width: 222px; height: 109px;
    background: var(--white);
    border: 3px solid var(--ink);
    border-radius: 40px;
    padding: 15px 0 0 24px;
    font-size: 19px; line-height: 25px; color: var(--ink);
    font-style: normal;
    white-space: nowrap;
  }
</style>
</head>
<body>
  <main class="billboard">
    <div class="band-top"></div>
    <div class="brand-title">BRIGHT MEADOW</div>
    <div class="tagline">WHERE PETS COME TO STAY, PLAY &amp; TRAIN!</div>

    <h1 class="headline">YOUR BEST FRIEND’S BEST DAY</h1>

    <div class="photo-left" role="img" aria-label="Photo of a brown hound dog peeking up over the bottom band"></div>
    <div class="photo-right" role="img" aria-label="Photo of a smiling white French bulldog with a red collar, paws over the band"></div>

    <ul class="services">
      <li>DOG BOARDING</li>
      <li>DOG GROOMING</li>
      <li>DOG DAYCARE</li>
      <li>DOG TRAINING</li>
    </ul>

    <div class="band-bottom"></div>

    <div class="brand-mark"><span class="dot"></span>Bright Meadow</div>

    <div class="contact">
      <p class="call">Call: <strong>(555) 014-2290</strong></p>
      <p class="line">Email: <strong>pawplayhub@mailnest.example</strong></p>
      <p class="line">web: <strong>www.pawplayhub.example</strong></p>
    </div>

    <address class="address">
      48 Willow Bend Rd.<br>Maple Falls, IA<br>50699
    </address>
  </main>
</body>
</html>
```